The Iron Trials Borinquen Coast (ITBC) – Sponsorship Proposal 2026 | Second Edition

We are looking to redesign and elevate our Sponsorship Proposal for the second edition of The Iron Trials Borinquen Coast (ITBC) - a Tactical Fitness competition that combines functional fitness and live-fire shooting in a safe and controlled environment.
The first edition (March 7, 2026) was a proven success, and the updated proposal must reflect that evolution from concept to validated event.
OBJECTIVE
Create a visually striking, premium, and highly structured sponsorship proposal that communicates:
- Credibility (proven event)
- Growth (scaling momentum)
- Experience (not just competition, but a full event)
----------------------------
KEY DATA TO INCLUDE (VERY IMPORTANT)
The design must highlight the following real metrics prominently:
- 96 registered athletes
- 240+ spectators
- 35 volunteers
- 370+ total attendees
- 14 female athletes
- 5 youth participants (ages 12–16)
- $3,300 awarded in prize money
INAUGURAL SPONSORS:
- Coastal Sky Corps
- Caribe Territorial Defense Reserve
- Harbor Militia Auxiliary
- Crestmoor Real Estate
- MTK (Mariposa Trek Kit)
- Quillstone Studio
- Reef Motion 442, KORVA San Juan
- Premier Dispatch PR
- Core Harmony
NEXT EVENT (IMPORTANT FOR DESIGN STORY)
- Event Date: December 19, 2026
- Expected Attendance:
- 130+ athletes
- 300+ spectators
- ~500 total attendees
- Theme: Christmas Experience
- Full event decorated in Christmas theme
- Food vendors + traditional Puerto Rican roasted pork (150+ lbs), community, and sponsor activations
👉 This is NOT just a competition - it is an experience-driven event.
STRUCTURE (BASED ON CURRENT PROPOSAL)
- Use the existing proposal as structural reference , but improve layout, hierarchy, and storytelling:
- Cover Page (modern + bold)
- Executive Summary (UPDATED with real results)
- Event Concept / Experience
- Audience & Attendance (with real + projected numbers)
- Sponsors (social proof section)
- Sponsorship Packages (Alpha = $10,000, Bravo = $1,000, Charlie = $500, Delta = $250)
- Why Sponsor ITBC
- Contact Page
EVENT DIVISIONS (UPDATED – VERY IMPORTANT)
The proposal must clearly showcase the five official competition divisions, with strong visual hierarchy (icons, images, or cards per division). This section should feel dynamic, premium, and easy to scan.
Divisions to include:
SCALE DIVISION (Adaptive)
An adaptive division for those who want to experience ITBC in a controlled environment.
No rankings. No prizes.
This is about completing the challenge.
BEGINNER DIVISION
For athletes ready to compete in a structured and approachable format.
Challenging, but accessible.
Athletes compete for placement.
INTERMEDIATE DIVISION
For athletes with a strong foundation in fitness and shooting.
Heavier loads. Higher standards.
Performance matters.
JÍBARO DIVISION (Elite)
The highest level of competition at ITBC.
Retention holsters required. Rifles carried in slings. Heavier loads.
Built for athletes who want to prove themselves.
MASTERS 45+ DIVISION
For athletes 45+ who want to compete while prioritizing longevity and control.
Maintains competitive intensity within an age-based category.
2-GUN FORMAT (IMPORTANT – INCLUDE BELOW DIVISIONS)
All divisions are available in either:
Pistol
2-Gun (Pistol + Rifle)
In the 2-Gun format, athletes utilize both pistol and rifle throughout the competition, transitioning between weapons under physical fatigue and time pressure.
DESIGN NOTE FOR THIS SECTION
Present divisions as individual visual blocks/cards (like the reference provided)
Use bold titles + short descriptions (keep text tight)
Include action images per division if possible
Highlight Jíbaro Division as the elite tier visually
Ensure this section is one of the most visually engaging pages in the proposal
DESIGN STYLE & VISUAL DIRECTION
We want a military / tactical / premium fitness aesthetic, similar to brands like:
- Brindle Athletics
- The Valor Circuit
- MeshLift-style event decks
Tone:
- Strong
- Clean
- Masculine but modern
- Minimal clutter
COLOR PALETTE (MANDATORY)
Use the following brand colors:
- Light Olive Green (#636B2F)
- Dark Olive Green (#3D4127)
- Sand / Khaki (#C2B280)
- Charcoal / Black (#1C1C1C)
- Light Gray (#D3D3D3)
- White (#FFFFFF)
- Accent Red (#C80018) – for highlights only
DESIGN NOTES
- Use bold typography (military/tactical feel - I will include the font called BOOTCAMP which is the main font used for the first edition)
- Strong use of contrast (dark backgrounds + light text)
- Icons for stats (athletes, spectators, etc.)
- Clean infographics for numbers
- Full-page images for impact (action shots, athletes, shooting, fitness)
- Official logo included (PNG and vectorized)
- Keep it visually dynamic but easy to read
IMPORTANT MESSAGE SHIFT
The proposal must clearly communicate:
- This is NOT a new event
- This is a proven concept that is scaling
Before: “Support us”
Now: “Join a growing movement early”
FINAL DELIVERABLE
- Print-ready PDF (high quality)
- Editable source file (Illustrator)
- Modern, clean layout with strong visual hierarchy
Website: www.theitbc-example.com
Instagram: https://www.instagram.com/theitbc_demo/
- BOOTCAMP

```html
<!DOCTYPE html>
<html lang="en">
<head>
<meta charset="utf-8">
<title>The Iron Trials Borinquen Coast – Sponsorship Proposal</title>
<link href="https://fonts.googleapis.com/css2?family=Black+Ops+One&family=Arimo:wght@400;700&display=swap" rel="stylesheet">
<style>
  :root {
    --red: #C80018;
    --charcoal: #1C1C1C;
    --sand: #C2B280;
    --gold: #BFA46A;
    --white: #FFFFFF;
    --gray: #D3D3D3;
    --muted: #8A8A86;
    --olive-dark: #3D4127;
  }
  * { margin: 0; padding: 0; box-sizing: border-box; }
  html, body { width: 927px; height: 1200px; overflow: hidden; background: var(--charcoal); }
  .cover {
    position: relative;
    width: 927px;
    height: 1200px;
    overflow: hidden;
    font-family: "Arimo", Arial, sans-serif;
    color: var(--white);
  }
  .cover-photo {
    position: absolute; inset: 0;
    background:
      radial-gradient(ellipse at 50% 60%, rgba(70,72,66,0.55) 0%, rgba(30,32,28,0) 60%),
      linear-gradient(180deg, #1d221b 0%, #262823 35%, #2a2a28 60%, #222220 100%);
  }
  .top-bar { position: absolute; top: 0; left: 0; width: 100%; height: 9px; background: var(--red); }
  .event-mark {
    position: absolute; top: 150px; left: 0; width: 100%;
    display: flex; flex-direction: column; align-items: center; gap: 14px;
  }
  .event-mark .mark-square { width: 58px; height: 58px; border: 3px solid var(--gray); }
  .event-mark .mark-name {
    font-family: "Black Ops One", "Arimo", sans-serif;
    font-size: 46px; letter-spacing: 6px; color: var(--gray);
  }
  .title-block { position: absolute; top: 326px; left: 0; width: 100%; text-align: center; }
  .title-the {
    font-family: "Black Ops One", sans-serif; font-size: 17px; letter-spacing: 1px;
  }
  .title-main {
    font-family: "Black Ops One", sans-serif; font-size: 56px; line-height: 1; margin-top: 12px; letter-spacing: 1px;
  }
  .title-sub {
    font-family: "Black Ops One", sans-serif; font-size: 42px; line-height: 1; margin-top: 18px; letter-spacing: 1px;
  }
  .title-rule {
    position: absolute; top: 514px; left: 313px; width: 301px; height: 2px; background: var(--gold);
  }
  .proposal-label {
    position: absolute; top: 533px; left: 0; width: 100%; text-align: center;
    font-family: "Black Ops One", sans-serif; font-size: 14px; color: var(--gold); letter-spacing: 0.5px;
  }
  .edition-line {
    position: absolute; top: 565px; left: 0; width: 100%; text-align: center;
    font-size: 15px; letter-spacing: 0.8px; color: var(--sand);
  }
  .edition-badge {
    position: absolute; top: 606px; left: 382px; width: 165px; height: 45px;
    background: var(--red); border-radius: 4px;
    display: flex; align-items: center; justify-content: center;
    font-family: "Black Ops One", sans-serif; font-size: 16px; letter-spacing: 0.5px;
  }
  .venue { position: absolute; top: 1066px; left: 0; width: 100%; text-align: center; font-size: 12.5px; line-height: 21px; }
  .prepared { position: absolute; top: 1126px; left: 0; width: 100%; text-align: center; font-size: 10.5px; line-height: 20px; color: var(--muted); }
</style>
</head>
<body>
  <main class="cover">
    <div class="cover-photo" role="img" aria-label="Darkened photo of a crowd of athletes gathered among event tents at the first edition"></div>
    <div class="top-bar"></div>

    <div class="event-mark">
      <div class="mark-square"></div>
      <div class="mark-name">ITBC</div>
    </div>

    <header class="title-block">
      <div class="title-the">THE</div>
      <h1 class="title-main">IRON TRIALS</h1>
      <div class="title-sub">BORINQUEN COAST</div>
    </header>

    <div class="title-rule"></div>
    <div class="proposal-label">SPONSORSHIP PROPOSAL</div>
    <div class="edition-line">SECOND EDITION &nbsp;|&nbsp; DECEMBER 19, 2026</div>
    <div class="edition-badge">EDITION II</div>

    <div class="venue">
      <div>Palmar Ridge Shooting Club &nbsp;|&nbsp; Cerro Verde, Borinquen Coast</div>
      <div>Tactical Fitness &amp; Live-Fire Competition</div>
    </div>

    <div class="prepared">
      <div>Prepared by Mateo R. Cordero, Founder &amp; CEO</div>
      <div>mateo@theitbc-example.com &nbsp;|&nbsp; 555-014-2290 &nbsp;|&nbsp; @theitbc_demo</div>
    </div>
  </main>
</body>
</html>
```